Vorgan Sports Nutrition Brand needs a Packaging label

Hi all, please see the considerations for our vision.
We need a Golden Ratio packaging label design for new Sports nutrition/supplement brand. I would like to give you a little bit of background about myself and hopefully that will help you in creating the design.
I am myself into fitness. I am 33 years old at the moment and been hitting gyms consistently from 14 years old. I do use supplements of all types that helps with performance and body compositions.
Ideally I would like the brand to be able to resonate with male and female audience. The brand needs to give premium look and feel. Those people who will be associating themselves with the brand should be proud of themselves being a part of the team. That's our ideal customer persona.
In terms of colours we are open to your suggestions but do think that red should be included as a detail colour.
P.S Please check out my Instagram to learn more about ideal customer for the brand. @pelmatovv
When creating the name ''vorgan'' we wanted the name to capture two things. First a feeling that we get when we go to gyms and the feeling is excited. And secondly the name for the product or the industry and that's nutrition. We then shortened the feeling excited to Vorgan for a more catchy name.

The Nutrition information will be sent to add once we pick the design.
The pictures of brands that we admire them are attached.

Please design One label design and just resize for these products. For dimensions please refer to the Print guide attached.
Core Bulk Builder 2.25KG
Tasty Strengthmix 250G
Vigor Lift Prime 120 Tabs
Surge Rush Pre Workout 250G
Branded Shakers

Target Market(s)

Fitness / bodybuilding audience male & female mass market

Industry/Entity Type

Nutrition

Colors

Designer to choose colors to be used in the design.

Requirements
Must have
• Our logo.
• Please find it attached
Nice to have
• The transparent Logo X some where in the background almost like a watermark. In other words like a subconscious clue.
Should not have
• Organic look.

```html
<!DOCTYPE html>
<html lang="en">
<head>
<meta charset="utf-8">
<title>Vorgan Nutrition – Workout Formula Label</title>
<link rel="stylesheet" href="https://fonts.googleapis.com/css2?family=Oswald:wght@500;700&family=Roboto+Condensed:wght@400;700&family=Archivo+Black&display=swap">
<style>
  :root{
    --bg:#ffffff;
    --ink:#0d0d0f;
    --panel:#121215;
    --red:#c4201c;
    --red-dark:#8f1412;
    --white:#f4f4f4;
    --grey:#bdbdbd;
    --grape:#c79be8;
    --skin-light:#a88a78;
    --skin-dark:#3a2a24;
  }
  *{margin:0;padding:0;box-sizing:border-box}
  html,body{width:1200px;height:1200px;overflow:hidden;background:var(--bg)}
  .canvas{position:relative;width:1200px;height:1200px}
  .label{position:absolute;left:43px;top:365px;width:1116px;height:288px;
    background:radial-gradient(ellipse at 40% 40%, #2a2a30 0%, var(--ink) 70%);overflow:hidden;
    font-family:"Roboto Condensed",Arial,sans-serif;color:var(--white)}
  .abs{position:absolute}
  .hero-glow{left:300px;top:0;width:480px;height:288px;
    background:radial-gradient(circle at 45% 45%, rgba(196,32,28,.55) 0%, rgba(196,32,28,.15) 45%, transparent 70%)}

  /* info panel */
  .info{left:14px;top:7px;width:197px;height:270px;border:1px solid #555;font-size:6.6px;line-height:1.42;text-align:justify}
  .info section{padding:3px 4px;border-bottom:1px solid #666}
  .info section:first-child{height:166px}
  .info section:last-child{border-bottom:none;font-weight:700}
  .info p+p{margin-top:7px}
  .info b{font-weight:700}

  /* vertical brand */
  .side-brand{left:258px;top:150px;transform:rotate(-90deg);width:0;height:0}
  .side-brand span{position:absolute;left:-110px;top:-42px;width:220px;height:56px;text-align:center;
    font-family:"Oswald",sans-serif;font-weight:700;font-size:56px;line-height:1;color:var(--white);white-space:nowrap}
  .side-brand em{position:absolute;left:-110px;top:26px;width:220px;text-align:center;font-style:normal;line-height:1;
    font-family:"Oswald",sans-serif;font-weight:500;font-size:11px;letter-spacing:8px;color:var(--white)}

  .athlete{left:321px;top:78px;width:190px;height:210px;border-radius:45% 45% 0 0;
    background:radial-gradient(ellipse at 50% 35%, var(--skin-light) 0%, #6d5548 45%, var(--skin-dark) 80%, transparent 100%)}

  .brand{left:381px;top:26px;width:300px;text-align:center}
  .brand-name{font-family:"Oswald",sans-serif;font-weight:700;font-size:64px;line-height:1;color:var(--white);letter-spacing:1px}
  .brand-sub{font-family:"Oswald",sans-serif;font-weight:500;font-size:15px;line-height:1;letter-spacing:10px;color:var(--white);margin-top:5px}

  .tag{font-family:"Oswald",sans-serif;font-weight:700;color:var(--white);background:var(--red);
    border:1.5px solid var(--white);white-space:nowrap;text-transform:uppercase;line-height:1.2}
  .tag-formula{left:496px;top:124px;font-family:"Archivo Black",sans-serif;font-weight:400;font-size:17px;padding:3px 7px}
  .tag-catabolic{left:533px;top:168px;font-size:14px;padding:0 5px;transform:rotate(-9deg);background:var(--red-dark)}
  .tag-ratio{left:590px;top:196px;font-size:14px;padding:0 5px;transform:rotate(6deg);background:var(--red-dark)}

  .servings{left:367px;top:252px;display:flex;align-items:center;gap:4px}
  .servings .count{font-family:"Archivo Black",sans-serif;font-size:18px;line-height:1;color:var(--white)}
  .servings .txt{font-family:"Oswald",sans-serif;font-weight:500;font-size:10px;background:var(--red);padding:1px 4px;text-transform:uppercase}

  .flavor{left:570px;top:238px;width:180px;text-align:center}
  .flavor-name{font-family:"Archivo Black",sans-serif;font-size:19px;line-height:1;color:var(--grape);white-space:nowrap}
  .flavor-note{font-family:"Oswald",sans-serif;font-weight:500;font-size:10px;line-height:1.2;margin-top:3px;color:var(--white);letter-spacing:.5px;white-space:nowrap}

  .claim{left:800px;top:140px;transform:rotate(-90deg);width:0;height:0}
  .claim div{position:absolute;left:-140px;width:280px;text-align:center;font-family:"Oswald",sans-serif;font-weight:700;
    font-size:22px;line-height:1;color:var(--white);white-space:nowrap;letter-spacing:.3px}
  .claim .l1{top:-28px}
  .claim .l2{top:4px}

  /* facts */
  .facts{left:877px;top:7px;width:198px;background:var(--panel);border:1px solid #777;padding:3px 4px;font-size:7.5px;line-height:1.3}
  .facts h2{font-family:"Archivo Black",sans-serif;font-size:15px;letter-spacing:2.3px;line-height:1.05;white-space:nowrap}
  .facts .hd{font-weight:700;border-bottom:3px solid var(--white);padding-bottom:2px}
  .facts table{width:100%;border-collapse:collapse}
  .facts th{font-size:5.5px;text-align:right;padding:2px 0;border-bottom:1px solid var(--white)}
  .facts td{padding:2px 0;border-bottom:1px solid #888}
  .facts td:nth-child(2),.facts td:nth-child(3){text-align:right}
  .facts td.name{font-weight:700}
  .facts .sub{font-weight:400;display:block;padding-left:6px}
  .facts .notes{font-size:5.5px;padding:2px 0;border-top:3px solid var(--white)}
  .facts .ingr{font-size:5.7px;text-align:justify;padding:2px 0;border-top:1px solid var(--white)}
  .facts .allergen{font-size:5.7px;padding:2px 0;border-top:1px solid var(--white)}
  .maker{left:875px;top:243px;font-size:5.5px;line-height:1.35;color:var(--grey)}
  .code-box{left:998px;top:241px;width:90px;height:33px;background:var(--white)}
</style>
</head>
<body>
<div class="canvas">
  <div class="label">
    <div class="abs hero-glow"></div>

    <div class="abs info">
      <section>
        <p><b>FORGE 3D</b> is a blend of 5000mg of Branched Chain Amino Acids and Glutamine for lean muscle and recovery. BCAAs are the most abundant amino acids found in muscle tissue, and are the most readily absorbed group of amino acids. <b>FORGE 3D</b> contains the ideal ratio of 2 parts Leucine to 1 part Isoleucine and Valine.*</p>
        <p>These amino acids increase protein synthesis and nitrogen retention, both essential to building lean muscle. BCAAs are metabolized directly in the muscle, and are considered "essential" because the body cannot build them from other compounds. Instead, they must come from diet or supplementation. Take your results to a whole new level with this great tasting drink. *</p>
      </section>
      <section><p><b>DIRECTIONS:</b> Mix 6.5G (1 Scoop) in 6 - 8 ounces of cold beverage. It will take a few minutes for all the powder to dissolve in the beverage. Best taken pre/post-workout or between meals.</p></section>
      <section><p><b>WARNING:</b> Consult with a physician prior to use if you have any medical conditions. Do not use if pregnant or lactating.</p></section>
      <section><p>* These statements have not been evaluated by the Food and Drug Administration. This product is not intended to diagnose, treat, cure or prevent any disease.</p></section>
    </div>

    <div class="abs side-brand"><span>VORGAN</span><em>NUTRITION</em></div>

    <div class="abs athlete" role="img" aria-label="Photo of a muscular bare-chested athlete's torso"></div>

    <div class="abs brand">
      <div class="brand-name">VORGAN</div>
      <div class="brand-sub">NUTRITION</div>
    </div>

    <div class="abs tag tag-formula">Workout Formula</div>
    <div class="abs tag tag-catabolic">Anti-Catabolic Agent</div>
    <div class="abs tag tag-ratio">Perfect Ratio of 2:1:1</div>

    <div class="abs servings"><span class="count">50</span><span class="txt">Servs Dietary Supplement</span></div>

    <div class="abs flavor">
      <div class="flavor-name">WICKED GRAPE</div>
      <div class="flavor-note">NATURAL &amp; ARTIFICIAL FALVOR</div>
    </div>

    <div class="abs claim"><div class="l1">L-GLUTAMINE FOR INCREASED</div><div class="l2">MUSCLE RECOVERY</div></div>

    <div class="abs facts">
      <h2>Supplement Facts</h2>
      <div class="hd">Serving Size: 6.5G (1 Scoop)<br>Servings Per Container: 50</div>
      <table>
        <tr><th></th><th>Amount Per<br>Serving</th><th>%Daily<br>Value**</th></tr>
        <tr><td class="name">Sodium</td><td>20 mg</td><td>1%</td></tr>
        <tr><td class="name">Potassium</td><td>40 mg</td><td>1%</td></tr>
        <tr><td class="name">Vitamin B6<span class="sub">(Pyridoxine HCl)</span></td><td>2.5 mg</td><td>125%</td></tr>
        <tr><td class="name">BCAA / Glutamine Blend<span class="sub">(L-Leucine, L-Isoleucine, L-Valine, L-Glutamine)</span></td><td>5000mg</td><td>†</td></tr>
      </table>
      <div class="notes">**Percent Daily Values are based upon a 2,000 calorie diet.<br>† Daily Value not Established</div>
      <div class="ingr"><b>Ingredients:</b> Citric Acid, Natural &amp; Artificial Flavors, Sucralose, Potassium Citrate, Sodium Chloride, Acesulfame Potassium, Silicon Dioxide, Red Dye 40, and Blue 1.</div>
      <div class="allergen"><b>Allergen, Warning:</b> Manufactured on equipment which processes products containing milk, eggs, soybeans, wheat, shellfish, fish oil, tree nuts, and peanut flavor.</div>
    </div>

    <div class="abs maker">Developed and<br>Distributed by:<br><b>COMPANY</b><br>Address<br>City, State Zipcode</div>
    <div class="abs code-box"></div>
  </div>
</div>
</body>
</html>
```